Attorney Website Design

I need a top quality attorney website layout designed. Here are some examples of what I feel are great websites:
http://www.brelmoradivorceattorney.example/
http://www.vethomirlawfirm.example/
http://www.plexfirm.example/
http://www.harrowgatecriminaldefensefirm.example/
http://www.qzfirm.example/
http://www.tolvermoorcriminaldefensefirm.example/
http://www.drennocriminalattorneys.example/
http://www.qzfirm.example/
What we like about these sites:
• The different layers
• Subtle designs, textures, curves
• 3 dimensional
• Floating effects
• Prominent phone number
• Location of Areas of Practice
• Request A Consultation Prominent
• Right side bar with practice areas
• Badges
• Clear Calls to Action
• Dynamic/Staying Top navigation when you scroll
The project will be for a home page and then also an interior page (should be similar to home page).
I want to make it understood I am looking for a design which is not a typical "template" site which I can find anywhere for $50. This budget and project is for a "Custom" website design. Please submit designs similar in quality to the samples links I have posted. Creativity is a MUST! The best way to explain this is, I want a design that I can feel it unique and original, not something that looks like 95% of all websites out there.
Owen
I just wanted everyone to know that so far I am not to pleased with any of the designs. I am not looking for cut/pasting of other peoples websites but ORIGINAL and CREATIVE work.
Industry/Entity Type
Attorney

```html
<!DOCTYPE html>
<html lang="en">
<head>
<meta charset="utf-8">
<title>Law Office of Halberd, Quenton &amp; Ashby</title>
<link href="https://fonts.googleapis.com/css2?family=Lato:wght@400;700&family=Playfair+Display:wght@400;700&display=swap" rel="stylesheet">
<style>
:root{
  --blue:#1f4f95;
  --link:#2a62b8;
  --gold:#e8b21c;
  --ink:#333;
  --muted:#777;
  --dark:#1b1b1b;
  --panel:#2a2a2a;
  --rule:#d8d8d8;
  --paper:#fafafa;
}
*{margin:0;padding:0;box-sizing:border-box}
html,body{width:913px;height:1200px;overflow:hidden}
body{position:relative;background:var(--paper);font-family:"Lato",sans-serif;color:var(--ink)}
a{color:var(--link)}

/* Top bar */
.topbar{position:absolute;left:0;top:0;width:913px;height:43px;background:#f4f4f4;border-bottom:1px solid #ddd}
.brand{position:absolute;left:196px;top:8px;width:131px;text-align:center}
.brand small{display:block;font-family:"Playfair Display",serif;font-size:6px;letter-spacing:.5px;color:#333}
.brand span{display:block;margin-top:2px;background:#444;color:#fff;font-family:"Playfair Display",serif;font-size:7.5px;padding:4px 0;letter-spacing:.4px;white-space:nowrap}
.phone-tab{position:absolute;left:663px;top:0;width:61px;height:16px;background:#fff;font-size:9px;font-weight:700;text-align:center;line-height:16px;color:#333}
.nav{position:absolute;left:428px;top:24px;display:flex;gap:14px;font-family:"Playfair Display",serif;font-size:7.5px}
.nav a{color:#444;text-decoration:none}
.nav a.active{color:var(--blue)}

/* Hero */
.hero{position:absolute;left:0;top:43px;width:913px;height:164px;background:linear-gradient(90deg,#e6e6e6,#cfcfcf 45%,#9a9a9a);overflow:hidden}
.hero-photo{position:absolute;left:453px;top:0;width:340px;height:164px;background:linear-gradient(100deg,#bdbdbd,#b89a7c 40%,#8c7a6a 70%,#a7a7a7)}
.hero-copy{position:absolute;left:180px;top:34px;width:295px;text-align:center}
.hero-copy h1{font-family:"Playfair Display",serif;font-weight:400;font-size:24px;color:#555;line-height:26px;white-space:nowrap}
.hero-copy .trust{display:flex;align-items:center;justify-content:center;gap:12px;margin-top:6px;height:34px}
.hero-copy .trust i{display:block;width:50px;height:3px;background:#b0b0b0}
.hero-copy .trust b{font-family:"Playfair Display",serif;font-size:30px;line-height:34px;color:var(--blue);letter-spacing:1px}
.hero-copy p{font-family:"Playfair Display",serif;font-size:11px;color:#555;margin-top:8px;line-height:13px}

/* Services band */
.services{position:absolute;left:0;top:207px;width:913px;height:117px;background:linear-gradient(180deg,#222,#2f2f2f 50%,#1b1b1b);display:flex;justify-content:center}
.service{width:133px;text-align:center;color:#fff;padding-top:12px;border-right:1px solid #3a3a3a}
.service:last-child{border-right:0}
.service h3{font-family:"Playfair Display",serif;font-weight:400;font-size:12px}
.service p{font-size:7px;line-height:11px;margin-top:8px;color:#ddd}
.btn{display:inline-block;margin-top:14px;background:var(--gold);color:#222;font-size:6px;font-weight:700;padding:4px 7px;letter-spacing:.3px}
.band-edge{position:absolute;left:0;top:324px;width:913px;height:4px;background:#9c9c9c}

/* Title */
.state-shape{position:absolute;left:197px;top:353px;width:50px;height:44px;background:linear-gradient(135deg,#e2e2e2,#cfcfcf)}
.page-title{position:absolute;left:253px;top:351px;font-family:"Playfair Display",serif;font-size:19px;color:var(--blue);letter-spacing:.5px;white-space:nowrap}
.page-sub{position:absolute;left:394px;top:378px;font-family:"Playfair Display",serif;font-size:14px;color:#777;letter-spacing:.5px}
.title-rule{position:absolute;left:197px;top:417px;width:520px;height:1px;background:var(--rule)}

/* Sidebar */
.sidebar{position:absolute;left:196px;top:440px;width:120px}
.sidebar-head{background:#9a9a9a;color:#fff;font-family:"Playfair Display",serif;font-size:13px;line-height:13px;text-align:center;padding:4px 0 5px;box-shadow:2px 2px 0 #ccc}
.practice{margin-top:8px;list-style:none}
.practice .group{padding:0;border:0;margin-top:5px}
.practice .group:first-child{margin-top:0}
.practice h4{font-size:7.5px;color:var(--blue);font-weight:700;padding:4px 0 3px 9px}
.practice li{font-size:6.8px;line-height:9px;color:#555;padding:3.3px 0 3.3px 18px;border-bottom:1px solid #e6e6e6;position:relative}
.practice li:not(.group)::before{content:"";position:absolute;left:10px;top:7px;width:2px;height:2px;background:#999}

/* Main */
.main{position:absolute;left:373px;top:440px;width:305px;font-size:7.2px;line-height:11px;color:#444}
.main h2{font-family:"Playfair Display",serif;font-weight:400;font-size:14px;line-height:18px;color:#333;margin-bottom:12px;white-space:nowrap}
.main p{margin-bottom:11px}
.main ul{margin:0 0 11px 22px;list-style:square;color:var(--link)}
.main ul li{line-height:11px}
.main h2.second{margin-top:26px}

/* Footer */
.foot-edge{position:absolute;left:0;top:963px;width:913px;height:4px;background:#8a8a8a}
.footer{position:absolute;left:0;top:967px;width:913px;height:233px;background:radial-gradient(ellipse at 50% 30%,#303030,#151515 75%)}
.cta{position:absolute;left:198px;top:34px;width:230px;color:#fff}
.cta h3{font-family:"Playfair Display",serif;font-weight:400;font-size:17px;line-height:20px}
.cta p{font-size:8px;line-height:11px;color:#ccc;margin-top:6px}
.cta b{color:var(--gold);font-weight:400}
.fcol{position:absolute;top:34px;color:#ddd}
.fcol h4{font-family:"Playfair Display",serif;font-weight:400;font-size:15px;color:#fff;padding-bottom:4px;border-bottom:1px solid #777;width:118px}
.fcol p{font-size:7px;line-height:9px;margin-top:8px}
.loc{left:465px}
.loc a{display:block;margin-top:9px;font-size:7px;font-weight:700;color:#5b9be0;text-decoration:none}
.contact{left:599px}
.contact p{margin-top:7px}
.contact span{font-size:5.5px;color:#aaa;margin-right:4px}
.foot-rule{position:absolute;left:0;top:137px;width:913px;height:1px;background:#3c3c3c}
.counties{position:absolute;left:195px;top:157px;width:524px;text-align:center;font-size:6px;line-height:8px;color:#ccc}
.copy{position:absolute;left:0;top:198px;width:913px;text-align:center;font-size:5.8px;color:#777}
.legal{position:absolute;left:0;top:207px;width:913px;text-align:center;font-size:5.8px;color:#888}
.legal span{margin:0 5px}
</style>
</head>
<body>

<header class="topbar">
  <div class="brand"><small>THE LAW OFFICE OF</small><span>HALBERD, QUENTON &amp; ASHBY</span></div>
  <div class="phone-tab">352.555.0148</div>
  <nav class="nav">
    <a class="active" href="#">HOME</a><a href="#">OUR FIRM</a><a href="#">ATTORNEYS</a><a href="#">PRACTICE AREAS</a><a href="#">BLOG</a><a href="#">CONTACT</a>
  </nav>
</header>

<section class="hero">
  <div class="hero-photo" role="img" aria-label="Photograph of a smiling father with his two children"></div>
  <div class="hero-copy">
    <h1>ATTORNEYS YOU CAN</h1>
    <div class="trust"><i></i><b>TRUST</b><i></i></div>
    <p>Working aggressively to protect you<br>and your family.</p>
  </div>
</section>

<section class="services">
  <div class="service"><h3>Family Law</h3><p>In many instances, we can<br>have your case dropped<br>before charges are even filed.</p><span class="btn">LEARN MORE</span></div>
  <div class="service"><h3>Divorce Law</h3><p>In many instances, we can<br>have your case dropped<br>before charges are even filed.</p><span class="btn">LEARN MORE</span></div>
  <div class="service"><h3>Paternity Law</h3><p>In many instances, we can<br>have your case dropped<br>before charges are even filed.</p><span class="btn">LEARN MORE</span></div>
  <div class="service"><h3>Injunctions</h3><p>In many instances, we can<br>have your case dropped<br>before charges are even filed.</p><span class="btn">LEARN MORE</span></div>
</section>
<div class="band-edge"></div>

<div class="state-shape" role="img" aria-label="Map outline of the state of Florida"></div>
<div class="page-title">LAW OFFICE OF HALBERD, QUENTON &amp; ASHBY</div>
<div class="page-sub">GAINESVILLE, FLORIDA</div>
<div class="title-rule"></div>

<aside class="sidebar">
  <div class="sidebar-head">PRACTICE<br>AREAS</div>
  <ul class="practice">
    <li class="group"><h4>Family Law</h4></li>
    <li>Time Sharing</li><li>Visitation</li><li>Child Relocation</li><li>Child Support</li>
    <li class="group"><h4>Divorce Law</h4></li>
    <li>Alimony/ Support</li><li>Business &amp; Divorce</li><li>Doctor's Divorce</li><li>Divorce Appeals</li><li>Divorce with Young Children</li><li>Equitable Distribution</li><li>High Asset Divorce</li>
    <li class="group"><h4>Paternity Law</h4></li>
    <li>Establishing Paternity</li><li>Disestablishing Paternity</li><li>Paternity &amp; Support</li>
    <li class="group"><h4>Injunctions</h4></li>
    <li>Domestic Violence Injunctions</li><li>Repeat Violence Injunctions</li><li>Dating Violence Injunctions</li><li>Sexual Violence Injunctions</li><li>For Petitioners</li><li>For Respondants</li><li>Termination of Injunctions</li><li>Extending Injunctions</li><li>Injunction Appeals</li>
  </ul>
</aside>

<main class="main">
  <h2>Protecting Your Legal Rights</h2>
  <p>At the Law Office of Halberd, Quenton &amp; Ashby, we are committed to making a positive difference in the lives of our clients. We handle legal issues that strike at the heart of an individual's rights and interests, including:</p>
  <ul><li><a href="#">Family Law</a></li><li><a href="#">Divorce Law</a></li><li><a href="#">Paternity Law</a></li><li><a href="#">Injunctions</a></li></ul>
  <p>In each of our practice areas, we are dedicated to providing personal, aggressive and comprehensive legal representation. Speak to an experienced attorney before making any decisions about your case. To contact our Gainesville law office, call <b>352-555-0148</b>, or contact us toll free at <b>866-555-0192</b>.</p>
  <h2 class="second">The Experience You Need When it Matters Most</h2>
  <p>If you are facing a serious legal challenge, you need an experienced litigator. Even if your case does not go to trial, you need an attorney that is respected for their willingness to take a case to trial.</p>
  <p>If opposing counsel knows that your attorney is not completely comfortable in the courtroom - or too inexperienced to present an effective case on your behalf at trial - your ability to obtain a favorable result will be significantly diminished.</p>
  <p>Attorneys <a href="#">Marcus Halberd</a> and <a href="#">Elliot Quenton</a> , are both former prosecutors. They have handled thousands of criminal cases. As skilled negotiators and trial lawyers, they have the ability to protect your rights in an important criminal or family law matter. Attorney <a href="#">Renata Ashby</a> is a board certified marital and family attorney which makes her an expert. Ms. Ashby also handles probate matters throughout the State of Florida.</p>
  <p>Attorney <a href="#">Dana Pell</a> is a former Assistant Public Defender and has spent years defending some of the most difficult, challenging and complex cases in our criminal justice system. She now puts that experience to work for our criminal clients in Gainesville, Ocala, Lake City and surrounding communities.</p>
  <p>We are ready to put our knowledge and experience to work for you. If you need an attorney who will fight to obtain the best possible result in your case and passionately defend your rights, <a href="#">contact The Law Office of Halberd, Quenton &amp; Ashby in Gainesville, Florida</a>.</p>
</main>

<div class="foot-edge"></div>
<footer class="footer">
  <div class="cta">
    <h3>Contact a Skilled Gainesville Family Attorney</h3>
    <p>For more information or to schedule a consultation,<br>call <b>352-555-0148</b> or contact our Florida law firm online.</p>
  </div>
  <div class="fcol loc">
    <h4>Our Location</h4>
    <p>2750 West Larkspur Road<br>Building C, Suite 4<br>Gainesville, FL 32600</p>
    <a href="#">MAP AND DIRECTIONS</a>
  </div>
  <div class="fcol contact">
    <h4>Contact Us:</h4>
    <p><span>LOCAL</span>352-555-0148</p>
    <p><span>TOLL FREE</span>866-555-0192</p>
    <p><span>FAX</span>352-555-0177</p>
  </div>
  <div class="foot-rule"></div>
  <p class="counties">We represent clients throughout North Central Florida, including Alachua County, Bradford County, Clay County, Gilchrist County, Marion County, Levy County, Columbia County, Putnam County, Union County, Gainesville, Ocala, Palatka, Bronson, Starke, Trenton, Lake Butler, Green Cove Springs, and Lake City.</p>
  <p class="copy">© 2014 by The Law Office of Halberd, Quenton &amp; Ashby. All rights reserved.</p>
  <p class="legal"><span>Disclaimer</span>|<span>Site Map</span>|<span>Privacy Policy</span></p>
</footer>

</body>
</html>
```